Personal Trainer and Corporate Health Business

I need a business card for a new company I'm starting in Australia called "Brisk Vitality Partners" I will be providing a Personal training service as well as corporate health in companies.
The service provided is to help promote an active and healthy lifstyle.
The design should communicate a healthy lifestyle and also the benefits that this can have on a personal level and in the corporate environment and the benefits that flow from that.

Target Market(s)

Members of the public and Corporate

Industry/Entity Type

Environment

Requirements
Must have
• Company logo attached
Look and feel fresh and modern

Tag line: "Actively promoting a healthier lifestyle"

Lewis Norgate
Managing Director

m: 0417 596 304
e: lewis@briskvitalitypartners.com.au

www.briskvitalitypartners.com.au
Nice to have
• Can be 1 or 2 sided

```html
<!DOCTYPE html>
<html lang="en">
<head>
<meta charset="utf-8">
<title>Brisk Vitality Partners – Business Card</title>
<link rel="stylesheet" href="https://fonts.googleapis.com/css2?family=Ubuntu:wght@400;500;700&display=swap">
<style>
  :root {
    --card-blue: #034c93;
    --fresh-green: #86c125;
    --paper: #ffffff;
    --ink-light: #ffffff;
  }
  * { margin: 0; padding: 0; box-sizing: border-box; }
  html, body {
    width: 1200px;
    height: 698px;
    overflow: hidden;
    background: var(--paper);
  }
  .canvas {
    position: relative;
    width: 1200px;
    height: 698px;
    background: var(--paper);
    font-family: "Ubuntu", sans-serif;
    color: var(--ink-light);
  }
  .card {
    position: absolute;
    left: 29px;
    top: 0;
    width: 1142px;
    height: 690px;
    background: var(--card-blue);
    overflow: hidden;
  }
  .rule {
    position: absolute;
    left: 0;
    width: 100%;
    height: 4px;
    background: var(--paper);
  }
  .rule--upper { top: 54px; }
  .rule--lower { top: 163px; }
  .name-band {
    position: absolute;
    left: 0;
    top: 62px;
    width: 100%;
    height: 95px;
    background: var(--fresh-green);
    display: flex;
    align-items: center;
    justify-content: center;
  }
  .holder-name {
    font-weight: 700;
    font-size: 42px;
    letter-spacing: 1px;
    color: var(--ink-light);
  }
  .brand {
    position: absolute;
    left: 130px;
    top: 318px;
    width: 380px;
    display: flex;
    flex-direction: column;
    align-items: center;
    gap: 14px;
  }
  .brand-dot {
    width: 34px;
    height: 34px;
    border-radius: 50%;
    background: var(--fresh-green);
  }
  .brand-name {
    font-weight: 500;
    font-size: 34px;
    line-height: 1.15;
    text-align: center;
    color: var(--ink-light);
  }
  .divider {
    position: absolute;
    left: 571px;
    top: 262px;
    width: 4px;
    height: 282px;
  }
  .contact {
    position: absolute;
    left: 636px;
    font-size: 30px;
    line-height: 42px;
    font-weight: 400;
    color: var(--ink-light);
  }
  .contact--direct { top: 277px; }
  .contact--address { top: 437px; }
  .tagline {
    position: absolute;
    left: 0;
    top: 612px;
    width: 100%;
    text-align: center;
    font-size: 30px;
    letter-spacing: 5.2px;
    font-weight: 400;
    color: var(--ink-light);
  }
</style>
</head>
<body>
<div class="canvas">
  <div class="card">
    <div class="rule rule--upper"></div>
    <div class="name-band">
      <h1 class="holder-name">Lewis</h1>
    </div>
    <div class="rule rule--lower"></div>

    <div class="brand">
      <span class="brand-dot"></span>
      <span class="brand-name">Brisk Vitality<br>Partners</span>
    </div>

    <svg class="divider" viewBox="0 0 4 282" preserveAspectRatio="none" aria-hidden="true">
      <path d="M2 0 L3 141 L2 282 L1 141 Z" fill="#ffffff"/>
    </svg>

    <div class="contact contact--direct">
      <p class="contact-phone">04152873316 (M)</p>
      <p class="contact-email">brisk.vitality@mailbox.com</p>
    </div>
    <div class="contact contact--address">
      <p>address will come here</p>
      <p>address will come here</p>
    </div>

    <p class="tagline">Actively promoting a healthier lifestyle</p>
  </div>
</div>
</body>
</html>
```